DROVA website redesign

DROVA provides situational safety training and equipment to give people the knowledge and skills to keep themselves safe, be effective and confident in their jobs. We want to redesign our current website, drova.co.nz, to make it look cleaner and more appealing. Our colour palette is grey, orange and red (of the logo). Our audience was traditionally government agencies, mainly staff in enforcement or compliance roles, but is increasingly anyone in a front facing role, including librarians, health sector and non-enforcement. We need to ensure we retain a feel of being the leading providers in this field, as well as appeal to wider audience.
The final design will feel clean, fresh, inviting and ensure the audience understands we are the leaders in this training field. We should emphasise both the face to face training and our increasing online portfolio.

```html
<!DOCTYPE html>
<html lang="en">
<head>
<meta charset="utf-8">
<title>DROVA – Situational Safety & Tactical Communications</title>
<link href="https://fonts.googleapis.com/css2?family=Rajdhani:wght@600;700&family=Roboto:wght@400;500;700&display=swap" rel="stylesheet">
<style>
:root{
  --red:#e3312c;
  --orange:#f1662c;
  --orange-2:#f5843a;
  --ink:#4a4a4c;
  --text:#6b6b6e;
  --muted:#9a9a9d;
  --pale:#f1f1f2;
  --dark:#58585b;
  --white:#fff;
}
*{box-sizing:border-box;margin:0;padding:0}
html,body{width:1200px;height:5333px;overflow:hidden}
body{font-family:"Roboto",sans-serif;color:var(--text);background:var(--white);position:relative}
h1,h2,h3,.display{font-family:"Rajdhani",sans-serif;font-weight:700;color:var(--ink);text-transform:uppercase}
.abs{position:absolute}
.btn{display:inline-flex;align-items:center;gap:8px;height:44px;padding:0 26px;border-radius:22px;background:var(--orange);color:#fff;font:700 15px "Roboto",sans-serif;text-transform:uppercase;text-decoration:none;white-space:nowrap}
.btn.red{background:var(--red)}
.btn .dot{width:14px;height:14px;border-radius:50%;background:#fff;position:relative}
.btn .dot::after{content:"";position:absolute;left:5px;top:4px;border-left:5px solid var(--orange);border-top:3px solid transparent;border-bottom:3px solid transparent}
.btn.red .dot::after{border-left-color:var(--red)}
.photo{background:linear-gradient(135deg,#7d8389,#b5b0a6 55%,#5c6168)}

/* header */
.site-header{position:absolute;top:0;left:0;width:1200px;height:105px;background:#fff}
.brand{position:absolute;left:110px;top:22px;font:700 64px "Rajdhani",sans-serif;color:var(--ink);letter-spacing:2px;line-height:1}
.topbar{position:absolute;right:110px;top:22px;display:flex;align-items:center;gap:20px;font-size:15px;color:var(--ink)}
.topbar .ic{color:var(--red);margin-right:6px}
.pill{height:36px;padding:0 20px;border-radius:18px;background:var(--red);color:#fff;display:flex;align-items:center;font-weight:500}
.pill.or{background:var(--orange)}
.nav{position:absolute;right:110px;top:78px;display:flex;gap:26px;font-size:15px;color:var(--ink);font-weight:500}

/* hero */
.hero{position:absolute;top:105px;left:0;width:1200px;height:665px;overflow:hidden}
.hero .photo{position:absolute;inset:0;background:linear-gradient(180deg,#8a8f96,#4a5566 60%,#2b3442)}
.hero h1{position:absolute;top:185px;width:100%;text-align:center;color:#fff;font-size:38px;line-height:46px;letter-spacing:.5px}
.hero .btn{position:absolute;left:500px;top:310px}

/* intro */
.intro h2{position:absolute;left:110px;top:850px;font-size:31px;line-height:41px;letter-spacing:.5px}
.intro .copy{position:absolute;left:560px;top:850px;width:530px;font-size:13.5px;line-height:25px}
.intro .copy p+p{margin-top:12px}

/* services */
.services{position:absolute;top:1240px;left:0;width:1200px;height:1745px;background:var(--pale)}
.sec-title{position:absolute;width:100%;text-align:center;font-size:38px}
.sec-title::after{content:"";display:block;width:60px;height:3px;background:var(--red);margin:8px auto 0}
.service h3{font-size:32px;margin-bottom:22px}
.service p{font-size:13.5px;line-height:27px;margin-bottom:12px}
.service{position:absolute;width:460px}
.service .actions{display:flex;gap:16px;margin-top:22px}
.shot{position:absolute;width:462px;height:325px;border:4px solid #fff;box-shadow:0 4px 14px rgba(0,0,0,.15)}

/* why */
.why h2{position:absolute;left:110px;top:3085px;font-size:38px}
.why ul{position:absolute;left:110px;top:3165px;list-style:none;font-size:14px}
.why li{height:34px;display:flex;align-items:center;gap:14px}
.why li svg{flex:none}
.circle{position:absolute;border-radius:50%;border:5px solid #fff;box-shadow:0 4px 12px rgba(0,0,0,.2)}

/* trusted */
.trusted{position:absolute;top:3545px;left:0;width:1200px;height:320px;background:linear-gradient(90deg,var(--red),var(--orange) 45%,var(--orange-2))}
.trusted h2{position:absolute;top:90px;width:100%;text-align:center;color:#fff;font-size:38px}
.partners{position:absolute;top:153px;left:118px;display:flex;gap:31px}
.partner{width:168px;height:86px;background:#fff;border-radius:6px;display:flex;align-items:center;justify-content:center}
.partner span{width:96px;height:30px;border-radius:4px;background:#d9dbde}
.arrow{position:absolute;top:180px;width:30px;height:30px;border-radius:50%;background:#fff}

/* social */
.social-title{position:absolute;top:3945px;width:100%;text-align:center;font-size:38px}
.post{position:absolute;top:4045px;width:305px;height:415px;background:#fff;box-shadow:0 4px 16px rgba(0,0,0,.14)}
.post .img{height:170px;position:relative}
.post .tag{position:absolute;left:10px;top:10px;background:#3d5a98;color:#fff;font-size:12px;padding:3px 8px}
.post .meta{display:flex;gap:12px;padding:14px 14px 10px;align-items:center}
.post .av{width:34px;height:34px;border-radius:50%;border:1px solid #ddd;font:700 9px "Rajdhani",sans-serif;color:var(--ink);display:flex;align-items:center;justify-content:center;flex:none}
.post .meta b{display:block;font-size:13px;color:var(--ink)}
.post .meta small{font-size:10px;color:var(--muted)}
.post p{padding:0 14px;font-size:13px;line-height:23px}
.post .foot{position:absolute;bottom:16px;left:14px;right:14px;border-top:1px solid #eee;padding-top:12px;font-size:11px;color:var(--muted);display:flex;gap:16px}

/* promo */
.promo{position:absolute;top:4530px;left:0;width:1200px;height:500px}
.promo-copy{position:absolute;left:470px;top:100px;width:680px;display:flex;flex-direction:column;align-items:flex-start}
.promo-copy h2{color:#fff;font-size:40px;line-height:46px;white-space:nowrap}
.promo-copy .sub{color:#fff;font-size:18px;font-weight:500;margin-top:14px}
.promo-copy .btn{margin-top:34px;background:var(--orange)}
.product{position:absolute;left:112px;top:75px;width:280px;height:280px;border-radius:50%;background:#fff;display:flex;align-items:center;justify-content:center}
.product div{width:240px;height:240px;border-radius:50%;border:3px solid var(--red);background:radial-gradient(circle,#f0a04a,#3a3535 60%,#f2f2f2 62%)}

/* footer */
.footer{position:absolute;top:4990px;left:0;width:1200px;height:343px;color:#fff}
.footer h4{font:500 15px "Roboto",sans-serif;margin-bottom:22px}
.fcol{position:absolute;top:40px;font-size:12px;line-height:16px}
.fcol li{list-style:none;margin-bottom:10px}
.contact-item{display:flex;gap:10px;margin-bottom:16px}
.contact-item b{display:block;font-size:10px}
.copyline{position:absolute;top:302px;left:110px;right:110px;display:flex;justify-content:space-between;font-size:12px}
</style>
</head>
<body>

<header class="site-header">
  <div class="brand">DROVA</div>
  <div class="topbar">
    <span><span class="ic">&#9742;</span>0800 376 820</span>
    <span style="color:#ccc">|</span>
    <span><span class="ic">&#9993;</span>info@drova.co.nz</span>
    <span class="pill">Online Store</span>
    <span class="pill or">Login</span>
  </div>
  <nav class="nav">
    <span>Home</span><span>About</span><span>Industries Served ▾</span><span>Training ▾</span><span>Online Training</span><span>Gear ▾</span><span>Advice</span><span>Contact</span>
  </nav>
</header>

<section class="hero">
  <div class="photo" role="img" aria-label="Trainer presenting to a seated class of uniformed officers"></div>
  <h1>The situational safety &amp; tactical<br>communications experts</h1>
  <a class="btn red" href="#">Get started <span class="dot"></span></a>
  <svg class="abs" style="left:0;bottom:0" width="1200" height="110" viewBox="0 0 1200 110">
    <path d="M0 20 Q600 140 1200 20 L1200 110 L0 110Z" fill="#fff"/>
    <path d="M0 20 Q600 140 1200 20 L1200 28 Q600 150 0 40Z" fill="var(--red)"/>
  </svg>
</section>

<section class="intro">
  <h2>Stay safe - physically,<br>emotionally and<br>professionally with DROVA</h2>
  <div class="copy">
    <p>Dealing with people is not always easy - especially when there is the potential for conflict. DROVA's training programmes give you, or your staff, the knowledge and skills to stay safe, be effective and deal confidently and professionally with people - in any situation.</p>
    <p>What sets DROVA apart from other training providers is our training delivery. Our team of experienced, engaging instructors teach proven skills and techniques, using real-life examples, making training relevant, entertaining and effective for anyone in a front line role.</p>
  </div>
  <a class="btn abs" style="left:560px;top:1102px" href="#">Learn more <span class="dot"></span></a>
</section>

<section class="services">
  <h2 class="sec-title" style="top:60px">What we do</h2>

  <div class="service" style="left:110px;top:200px">
    <h3>Face to face training</h3>
    <p>Interacting safely, effectively and professionally with other people, especially within a regulatory environment or where a potential for conflict exists, requires specific knowledge and skills.</p>
    <p>DROVA offers a range of range of courses for anyone working in a front-line role, to give them proven skills,</p>
    <div class="actions"><a class="btn" href="#">Learn more <span class="dot"></span></a></div>
  </div>
  <div class="shot photo" style="left:628px;top:185px" role="img" aria-label="Instructor leading a classroom session by large windows"></div>

  <div class="shot photo" style="left:110px;top:563px" role="img" aria-label="Boardroom training with a video call on screen"></div>
  <div class="service" style="left:628px;top:582px">
    <h3>Online learning</h3>
    <p>We found the blended learning SSTC course an excellent option for us. In our operational roles taking people out for two days can be challenging whereas this option allows people to work at their own pace on-line then have a one day face to face session embedding their learnings."</p>
    <div class="actions"><a class="btn" href="#">Learn more <span class="dot"></span></a></div>
  </div>

  <div class="service" style="left:110px;top:955px">
    <h3>Gear</h3>
    <p>DROVA Systems is proud to represent world-class brands here in New Zealand. All products within the DROVA Systems range have been extensively tested by us before being DROVA-ified fit for purpose.</p>
    <p>As operational compliance and enforcement officers ourselves we know the importance of quality, functionality,</p>
    <div class="actions"><a class="btn" href="#">Learn more <span class="dot"></span></a><a class="btn red" href="#">Online store <span class="dot"></span></a></div>
  </div>
  <div class="shot" style="left:628px;top:940px;background:linear-gradient(160deg,#6f7d62,#8e9a83 50%,#3e4a3a)" role="img" aria-label="Officers practising tactical drills outdoors among trees"></div>

  <div class="shot photo" style="left:110px;top:1318px" role="img" aria-label="Trainer presenting to a group seated at tables"></div>
  <div class="service" style="left:628px;top:1337px">
    <h3>Advice</h3>
    <p>Organisations that are truly focussed on staff safety and effectiveness have the right policies in place, adopt best practise and design their workplaces with safety at the forefront.</p>
    <p>DROVA can assist in all these areas: we offer needs analysis, framework and policy development, workplace audits</p>
    <div class="actions"><a class="btn" href="#">Learn more <span class="dot"></span></a></div>
  </div>
</section>

<section class="why">
  <h2>Why choose DROVA</h2>
  <ul>
    <li><svg width="14" height="14"><circle cx="7" cy="7" r="7" fill="var(--red)"/><path d="M4 7l2 2 4-4" stroke="#fff" stroke-width="1.6" fill="none"/></svg>Lorem ipsum dolor sit amet, consectetur adipiscing elit, sed do Eiusmod</li>
    <li><svg width="14" height="14"><circle cx="7" cy="7" r="7" fill="var(--red)"/><path d="M4 7l2 2 4-4" stroke="#fff" stroke-width="1.6" fill="none"/></svg>tempor incididunt ut labore et dolore magna aliqua.</li>
    <li><svg width="14" height="14"><circle cx="7" cy="7" r="7" fill="var(--red)"/><path d="M4 7l2 2 4-4" stroke="#fff" stroke-width="1.6" fill="none"/></svg>Ut enim ad minim veniam, quis nostrud exercitation ullamco Laboris</li>
    <li><svg width="14" height="14"><circle cx="7" cy="7" r="7" fill="var(--red)"/><path d="M4 7l2 2 4-4" stroke="#fff" stroke-width="1.6" fill="none"/></svg>Nisi ut aliquip ex ea commodo consequat.</li>
    <li><svg width="14" height="14"><circle cx="7" cy="7" r="7" fill="var(--red)"/><path d="M4 7l2 2 4-4" stroke="#fff" stroke-width="1.6" fill="none"/></svg>Duis aute irure dolor in reprehenderit in voluptate velit</li>
    <li><svg width="14" height="14"><circle cx="7" cy="7" r="7" fill="var(--red)"/><path d="M4 7l2 2 4-4" stroke="#fff" stroke-width="1.6" fill="none"/></svg>Esse cillum dolore eu fugiat nulla pariatur.</li>
    <li><svg width="14" height="14"><circle cx="7" cy="7" r="7" fill="var(--red)"/><path d="M4 7l2 2 4-4" stroke="#fff" stroke-width="1.6" fill="none"/></svg>Excepteur sint occaecat cupidatat non proident, sunt</li>
    <li><svg width="14" height="14"><circle cx="7" cy="7" r="7" fill="var(--red)"/><path d="M4 7l2 2 4-4" stroke="#fff" stroke-width="1.6" fill="none"/></svg>Culpa qui officia deserunt mollit anim id est laborum.</li>
  </ul>
  <div class="circle photo" style="left:710px;top:3068px;width:380px;height:380px" role="img" aria-label="Presenter standing in front of a projector screen"></div>
  <div class="circle" style="left:655px;top:3230px;width:225px;height:225px;background:linear-gradient(140deg,#5b6a45,#c9c34a 50%,#2f3638)" role="img" aria-label="Security officer in high-visibility vest"></div>
</section>

<section class="trusted">
  <h2>Trusted to deliver</h2>
  <div class="arrow" style="left:44px"></div>
  <div class="partners">
    <div class="partner"><span></span></div>
    <div class="partner"><span></span></div>
    <div class="partner"><span></span></div>
    <div class="partner"><span></span></div>
    <div class="partner"><span></span></div>
  </div>
  <div class="arrow" style="right:44px"></div>
</section>

<h2 class="social-title">Keep social with DROVA</h2>
<article class="post" style="left:110px">
  <div class="img" style="background:linear-gradient(135deg,#2c3440,#6b4b44 50%,#1f2328)" role="img" aria-label="Magazine spread featuring safety lights"><span class="tag">Social</span></div>
  <div class="meta"><span class="av">DROVA</span><div><b>DROVA</b><small>october 8, 2021 3:51 pm</small></div></div>
  <p>Great review of our Beacon Guard lights in the 'Outdoor Edge' magazine (additional publication within the Coastal Angler News</p>
  <div class="foot"><span>↩</span><span>⟲ 10</span><span>♡ 63</span></div>
</article>
<article class="post" style="left:447px">
  <div class="img" style="background:linear-gradient(180deg,#5a7fa8,#1f2a3a)" role="img" aria-label="Three uniformed officers standing outdoors"><span class="tag">Social</span></div>
  <div class="meta"><span class="av">DROVA</span><div><b>DROVA</b><small>october 8, 2021 3:51 pm</small></div></div>
  <p>Great review of our Beacon Guard lights in the 'Outdoor Edge' magazine (additional publication within the Coastal Angler News</p>
  <div class="foot"><span>↩</span><span>⟲ 10</span><span>♡ 63</span></div>
</article>
<article class="post" style="left:783px">
  <div class="img" style="background:linear-gradient(160deg,#8d7a63,#4a4034)" role="img" aria-label="Empty training room with tables and chairs"><span class="tag">Social</span></div>
  <div class="meta"><span class="av">DROVA</span><div><b>DROVA</b><small>october 8, 2021 3:51 pm</small></div></div>
  <p>Great review of our Beacon Guard lights in the 'Outdoor Edge' magazine (additional publication within the Coastal Angler News</p>
  <div class="foot"><span>↩</span><span>⟲ 10</span><span>♡ 63</span></div>
</article>

<section class="promo">
  <svg class="abs" style="left:0;top:0" width="1200" height="500" viewBox="0 0 1200 500">
    <path d="M0 20 L1200 0 L1200 500 L0 500Z" fill="var(--red)"/>
  </svg>
  <div class="product" role="img" aria-label="Beacon Guard personal safety light unit"><div></div></div>
  <div class="promo-copy">
    <h2>Christmas special! Beacon Guard<br>personal safety lights</h2>
    <div class="sub">10% off until Christmas.</div>
    <a class="btn" href="#">Shop now</a>
  </div>
</section>

<footer class="footer">
  <svg class="abs" style="left:0;top:0" width="1200" height="343" viewBox="0 0 1200 343">
    <path d="M0 30 Q300 -10 600 20 T1200 0 L1200 343 L0 343Z" fill="var(--dark)"/>
  </svg>
  <div class="abs" style="left:140px;top:95px;font:700 64px 'Rajdhani',sans-serif;letter-spacing:2px">DROVA</div>
  <div class="abs" style="left:152px;top:175px;display:flex;gap:12px">
    <span style="width:12px;height:12px;border-radius:50%;background:#fff"></span>
    <span style="width:12px;height:12px;border-radius:50%;background:#fff"></span>
    <span style="width:12px;height:12px;border-radius:50%;background:#fff"></span>
    <span style="width:12px;height:12px;border-radius:50%;background:#fff"></span>
  </div>
  <div class="fcol" style="left:368px">
    <h4>Our Office Address</h4>
    <div class="contact-item"><span style="color:var(--red)">&#9742;</span><div><b>Phone</b>0800 376 820</div></div>
    <div class="contact-item"><span style="color:var(--red)">&#9993;</span><div><b>Email</b>info@drova.co.nz</div></div>
    <div class="contact-item"><span style="color:var(--red)">&#9679;</span><div><b>Location</b>Lorem ipsum dolor consectetur<br>adipiscing elit, sed do</div></div>
  </div>
  <div class="fcol" style="left:662px">
    <h4>Company</h4>
    <ul><li>Home</li><li>About Us</li><li>Services</li><li>Job Opportunities</li><li>Contact</li><li>About Me</li></ul>
  </div>
  <div class="fcol" style="left:862px;width:240px">
    <h4>Stil have questios?</h4>
    <p>Contact us using this form. A representa-tive will aswer your questions as soon as possible.</p>
    <a class="btn red" style="margin-top:24px;height:38px;padding:0 52px" href="#">Get a quote</a>
  </div>
  <div class="abs" style="right:110px;top:268px;background:#fff;color:var(--ink);font-size:10px;font-weight:700;padding:3px 12px;border-radius:10px">↑ Go Up</div>
  <div class="copyline"><span>© 2021 drova | All Rights Reserved</span><span>Privacy Policy &nbsp;|&nbsp; Cookie Policy &nbsp;|&nbsp; Terms Of Services</span></div>
</footer>

</body>
</html>
```